Zo Fen smart screen Flyer design

Hi,

Please see attached file as I have done up a very very basic flyer just with the information that will need to be presented.

Please don't go with this as a format I would like, as I have no design skills at all.

I'm looking for something that is basic but professional looking capturing this information.
I would prefer if the symbols were changed so they were all consistent and the colour scheme worked together with the logo.

If you can use the picture of the screen provided as I will replace this once my product has its photoshoot.

Thanks!

```html
<!DOCTYPE html>
<html lang="en">
<head>
<meta charset="utf-8">
<title>Zo Fen Smart Screen Flyer</title>
<link href="https://fonts.googleapis.com/css2?family=Montserrat:ital,wght@0,300;0,400;0,500;0,600;0,700;1,300;1,700&display=swap" rel="stylesheet">
<style>
  :root {
    --sky: #6cc6db;
    --teal-band: #66c3bc;
    --teal-deep: #3eb39b;
    --green-soft: #7ec98e;
    --accent-green: #2fae6e;
    --ink: #333a3f;
    --ink-soft: #3d4448;
    --white: #ffffff;
  }
  * { margin: 0; padding: 0; box-sizing: border-box; }
  html, body { width: 848px; height: 1200px; overflow: hidden; background: var(--white); }
  body { font-family: "Montserrat", Arial, sans-serif; }
  .flyer { position: relative; width: 848px; height: 1200px; overflow: hidden; }
  .backdrop { position: absolute; inset: 0; width: 848px; height: 1200px; }

  .brand {
    position: absolute; left: 40px; top: 48px; width: 210px;
    display: flex; align-items: center; gap: 12px;
    font-weight: 700; font-size: 34px; letter-spacing: 1px; color: var(--ink);
    text-transform: uppercase;
  }
  .brand-dot { width: 14px; height: 14px; background: var(--ink); }

  .screen-placeholder {
    position: absolute; left: 346px; top: 172px; width: 400px;
    text-align: center; color: var(--white);
    font-weight: 500; font-size: 31px; line-height: 43px;
  }

  .headline {
    position: absolute; left: 47px; top: 404px; width: 400px;
    color: var(--white); font-weight: 700; font-style: italic;
    font-size: 37px; line-height: 44px; text-transform: uppercase;
  }
  .subhead {
    position: absolute; left: 47px; top: 552px; width: 380px;
    color: var(--white); font-weight: 300; font-style: italic;
    font-size: 27.5px; line-height: 38px; text-transform: uppercase;
  }
  .intro {
    position: absolute; left: 47px; top: 672px; width: 361px;
    color: var(--white); font-weight: 300; font-size: 19.5px; line-height: 27.5px;
    text-align: justify; letter-spacing: 0.3px;
  }

  .contacts { position: absolute; left: 44px; top: 1012px; list-style: none; }
  .contact { display: flex; align-items: flex-start; gap: 26px; height: 60px; color: var(--white); }
  .contact svg { width: 28px; height: 28px; flex: none; }
  .contact-text { font-weight: 300; font-size: 17px; line-height: 22px; }
  .contact-note { display: block; font-size: 9px; line-height: 10px; opacity: 0.85; }

  .features { position: absolute; left: 567px; top: 0; list-style: none; }
  .feature { position: absolute; left: 0; width: 262px; }
  .feature-icon { position: absolute; left: -82px; top: 0; width: 44px; height: 44px; }
  .feature-title { color: var(--accent-green); font-weight: 700; font-size: 21px; line-height: 27px; }
  .feature-text { margin-top: 6px; color: var(--ink-soft); font-weight: 400; font-size: 14.5px; line-height: 19.5px; width: 250px; }
</style>
</head>
<body>
<main class="flyer">
  <svg class="backdrop" viewBox="0 0 595 842" preserveAspectRatio="none" aria-hidden="true">
    <defs>
      <linearGradient id="panelGreen" x1="0" y1="0" x2="0" y2="1">
        <stop offset="0" stop-color="#3eb39b"/>
        <stop offset="1" stop-color="#7ec98e"/>
      </linearGradient>
    </defs>
    <rect width="595" height="842" fill="#6cc6db"/>
    <polygon points="0,250 317,160 595,250 595,325 317,325 317,842 0,842" fill="#66c3bc"/>
    <polygon points="0,232 317,205 317,842 0,842" fill="url(#panelGreen)"/>
    <rect x="317" y="322" width="278" height="520" fill="#ffffff"/>
    <polygon points="0,0 200,0 200,78 95,122 0,78" fill="#ffffff"/>
  </svg>

  <div class="brand"><span class="brand-dot"></span>Zo Fen</div>

  <p class="screen-placeholder" role="img" aria-label="Area for a photo of an LED screen">YOUR LED SCREEN<br>IMAGE HERE</p>

  <h1 class="headline">Bring<br>attnetion to<br>your bussiness</h1>
  <p class="subhead">With your own HD<br>LED display.</p>
  <p class="intro">Our displays can be mounted outdoors on walls, roofs, fixed signs, trailer mounted ect. We also do indoor led screens for shop fronts and display stands. All screens are cumtom built to your requirements including size, shape and even curved displays</p>

  <ul class="contacts">
    <li class="contact">
      <svg viewBox="0 0 24 24" fill="none" stroke="#fff" stroke-width="2.2"><circle cx="12" cy="12" r="4"/><path d="M16 8v5.5a2.5 2.5 0 0 0 5 0V12a9 9 0 1 0-3.5 7.1"/></svg>
      <span class="contact-text">1300 ZOFENSC<span class="contact-note">for a free quote</span></span>
    </li>
    <li class="contact">
      <svg viewBox="0 0 24 24" fill="none" stroke="#fff" stroke-width="1.6"><circle cx="12" cy="12" r="10"/><ellipse cx="12" cy="12" rx="4.5" ry="10"/><path d="M2 12h20M4 6.5h16M4 17.5h16"/></svg>
      <span class="contact-text">www.zofenscreens.com.au</span>
    </li>
    <li class="contact">
      <svg viewBox="0 0 24 24" fill="#fff"><path d="M1 5h22v2.2l-11 7-11-7z"/><path d="M1 9.5l11 7 11-7V20H1z"/></svg>
      <span class="contact-text">info@zofenscreens.com.au</span>
    </li>
  </ul>

  <ul class="features">
    <li class="feature" style="top:524px">
      <svg class="feature-icon" viewBox="0 0 44 44" fill="#2fae6e"><text x="2" y="14" font-family="Montserrat, sans-serif" font-size="11" font-weight="600">4G</text><rect x="6" y="34" width="5" height="8"/><rect x="14" y="28" width="5" height="14"/><rect x="22" y="20" width="5" height="22"/><rect x="30" y="10" width="5" height="32"/></svg>
      <h2 class="feature-title">4G Capable</h2>
      <p class="feature-text">Change screen content with a click of the mouse anywhere in the world</p>
    </li>
    <li class="feature" style="top:638px">
      <svg class="feature-icon" viewBox="0 0 44 44" fill="none" stroke="#2fae6e" stroke-width="3.5" stroke-linecap="round"><path d="M4 18a26 26 0 0 1 36 0"/><path d="M10 25a17 17 0 0 1 24 0"/><path d="M16 32a8 8 0 0 1 12 0"/><circle cx="22" cy="38" r="1.5" fill="#2fae6e"/></svg>
      <h2 class="feature-title">Wifi Capable</h2>
      <p class="feature-text">Change screen content with a PC, tablet or mobile phone with an easy to use app</p>
    </li>
    <li class="feature" style="top:756px">
      <svg class="feature-icon" viewBox="0 0 44 44"><rect x="4" y="4" width="36" height="36" fill="#2fae6e"/><polygon points="40,4 40,40 4,40" fill="#ffffff" opacity="0.25"/><path d="M10 14h9M30 25v10M25 30h10" stroke="#fff" stroke-width="2.5"/></svg>
      <h2 class="feature-title">Inteligent brightness<br>control</h2>
      <p class="feature-text">Screen will automatically adjust to suit ambiant light improving screen veiwing quality and saving in power consumption</p>
    </li>
    <li class="feature" style="top:922px">
      <svg class="feature-icon" viewBox="0 0 44 44" fill="none" stroke="#2fae6e" stroke-width="2.2"><text x="0" y="14" font-family="Montserrat, sans-serif" font-size="12" font-weight="600" fill="#2fae6e" stroke="none">°C</text><path d="M22 6a4 4 0 0 1 8 0v22a8 8 0 1 1-8 0z"/><circle cx="26" cy="34" r="3.5" fill="#2fae6e"/><path d="M26 30V14M33 10h5M33 16h5M33 22h5"/></svg>
      <h2 class="feature-title">Online Monitoring</h2>
      <p class="feature-text">Monitor cabinet temperature and humidity plus more in real time online.<br>Recieve alerts via emial.</p>
    </li>
    <li class="feature" style="top:1056px">
      <svg class="feature-icon" viewBox="0 0 44 44" fill="none" stroke="#2fae6e" stroke-width="2.2"><circle cx="22" cy="17" r="13"/><circle cx="22" cy="17" r="8"/><path d="M13 27l-4 13 6-3 4 5 3-10M31 27l4 13-6-3-4 5-3-10"/></svg>
      <h2 class="feature-title">High quality products</h2>
      <p class="feature-text">Setting high standard for colour, brightness and sharpness these LED modules will create attention.</p>
    </li>
  </ul>
</main>
</body>
</html>
```